Oil and gas industry project solutions company needs professional cards with Canadian aboriginal fee

We are a aboriginally owned company that is focused on Project Planning, Management, Inspection & Consulting for Canada's Petroleum Industry. We have a logo that we would like to incorporate into a professional looking business card. We are professionals that offer services from project inception to completion.

Target Market(s)

Major industry leaders like NorvaLine, Brisk, Vorkantrel, Pelquist etc.

Industry/Entity Type

Industry

Contact Information for Business Card

Milo Rensford
milo@orvelpike.ca
250 555 0187

Requirements
Must have
• OrvelPike Inc. logo.
• Address is: RR4, Site2, Comp17 Fort St. John, BC V9X 2K3 Traditional Territory of the Treaty 8 People
• Colors that are in logo
• Banner or picture on back
• Ability to put different names and contacts
• Website: orvelpike.ca
• "Project Planning, Management, Inspection & Consulting for Canada's Petroleum Industry"

```html
<!DOCTYPE html>
<html lang="en">
<head>
<meta charset="utf-8">
<title>OrvelPike Inc. – Business Card</title>
<link rel="stylesheet" href="https://fonts.googleapis.com/css2?family=Source+Sans+3:wght@400;600;700&display=swap">
<style>
  :root {
    --stage: #000000;
    --paper: #ffffff;
    --brand-green: #6db344;
    --brand-green-deep: #5c9e36;
    --brand-navy: #23307a;
    --ink: #222222;
  }
  * { margin: 0; padding: 0; box-sizing: border-box; }
  html, body { width: 1200px; height: 900px; overflow: hidden; background: var(--stage); }
  body { position: relative; font-family: "Source Sans 3", "Myriad Pro", sans-serif; }

  .card { position: absolute; top: 275px; width: 477px; height: 293px; overflow: hidden; }
  .card--front {
    left: 116px; background: var(--paper);
    border-radius: 0 56px 0 56px;
  }
  .card--back {
    left: 622px; top: 276px; height: 292px; background: var(--brand-green);
    border-radius: 56px 0 56px 0;
  }

  .back-motif {
    position: absolute; left: 0; top: 0; width: 230px; height: 100%;
    background: linear-gradient(100deg, var(--brand-green-deep) 0%, rgba(92,158,54,0.55) 55%, rgba(109,179,68,0) 100%);
  }

  .brand-mark { position: absolute; display: flex; flex-direction: column; align-items: center; }
  .card--front .brand-mark { left: 20px; width: 246px; top: 48px; }
  .brand-mark__dot { width: 92px; height: 92px; border-radius: 50%; background: var(--brand-green); margin-bottom: 30px; }
  .brand-mark__name {
    font-weight: 700; font-size: 34px; letter-spacing: -0.3px; white-space: nowrap; color: var(--brand-navy);
  }
  .card--back .brand-mark { left: 150px; width: 310px; top: 196px; }
  .card--back .brand-mark__name { color: var(--paper); font-size: 37px; }

  .holder-name {
    position: absolute; right: 29px; top: 33px;
    font-weight: 600; font-size: 18.5px; color: var(--brand-green);
  }

  .contact-list { position: absolute; right: 29px; top: 152px; list-style: none; text-align: right; }
  .contact-list li {
    display: flex; justify-content: flex-end; align-items: center; gap: 6px;
    font-size: 13.5px; color: var(--ink); height: 20px;
  }
  .contact-list svg { width: 10px; height: 10px; fill: var(--brand-green); }

  .address {
    position: absolute; right: 29px; top: 229px; text-align: right;
    font-size: 13.5px; line-height: 18px; color: var(--ink); font-style: normal;
  }
</style>
</head>
<body>
  <section class="card card--front" aria-label="Business card front">
    <div class="brand-mark">
      <span class="brand-mark__dot"></span>
      <span class="brand-mark__name">OrvelPike Inc.</span>
    </div>

    <h1 class="holder-name">Milo Rensford</h1>

    <ul class="contact-list">
      <li>250 555 0187
        <svg viewBox="0 0 10 10" aria-hidden="true"><path d="M2 0.5 L3.6 2.6 L2.8 3.6 C3.5 5 5 6.5 6.4 7.2 L7.4 6.4 L9.5 8 L8.3 9.5 C4.5 9.2 0.8 5.5 0.5 1.7 Z"/></svg>
      </li>
      <li>milo@orvelpike.ca
        <svg viewBox="0 0 10 10" aria-hidden="true"><path d="M0.5 2 H9.5 V8.5 H0.5 Z M1.2 2.6 L5 5.4 L8.8 2.6" stroke="#fff" stroke-width="0.7"/></svg>
      </li>
      <li>www.orvelpike.ca
        <svg viewBox="0 0 10 10" aria-hidden="true"><circle cx="5" cy="5" r="4.6"/><path d="M0.5 5 H9.5 M5 0.5 C3 3 3 7 5 9.5 M5 0.5 C7 3 7 7 5 9.5" stroke="#fff" stroke-width="0.6" fill="none"/></svg>
      </li>
    </ul>

    <address class="address">RR4, Site2, Comp17 Fort<br>St. John, BC V9X 2K3</address>
  </section>

  <section class="card card--back" aria-label="Business card back">
    <div class="back-motif" role="img" aria-label="Faint enlarged brand symbol in tonal green"></div>
    <div class="brand-mark">
      <span class="brand-mark__name">OrvelPike Inc.</span>
    </div>
  </section>
</body>
</html>
```